Design business cards for Ironvale Barbers (Opening March so won't need finalised till January2018

Ironvale Barbers is the new age barbers and skincare for all men. Creating tailor made haircuts & customised skincare solutions for the perfect healthy manly look. The Barbers will have a industrial, rustic, worldly feel about it. Rustic red brick wall with old wine barrels as the work stations with the old fashion barber chairs. Concrete floor and a bit corrugated iron around.
Target Market(s)
Professional males who like a great haircut, wet shave and may consider a facial if in the right environment. Total pampering experience in a boys environment.
Industry/Entity Type
Barber
Contact Information for Business Card
Front- Logo - address is 42 Kowhai Rd Taupo
Ph - (07) 548 9163
www.ironvalebarbers.com
email - hello@ironvale.co.nz
Back of card
Mens Haircare - Wet Shaving - Facials - Skin Prescriptions
We are doing a loyalty program - 6 squares numbered then 7th free
Colors
Designer to choose colors to be used in the design.
Requirements
Must have
- Clean simple easy to read.
Nice to have
- Our current colours are white font on black background but thinking we need to introduce another colour. Maybe white logo on a copper, bronze or rusty background. Or even a rustic red brick wall with white writing. Want it clean simple to read. Maybe a burgundy?
Should not have
- no images like heads, scissors, razors please

```html
<!DOCTYPE html>
<html lang="en">
<head>
<meta charset="utf-8">
<title>Ironvale Barbers – Business Cards</title>
<link rel="stylesheet" href="https://fonts.googleapis.com/css2?family=Oswald:wght@400;600&display=swap">
<style>
  :root {
    --backdrop: #1f2022;
    --card-black: #1b1a19;
    --card-kraft: #c3a07c;
    --copper: #b38c66;
    --ink-dark: #2b1f16;
    --rule-grey: #a3a3a3;
  }
  * { margin: 0; padding: 0; box-sizing: border-box; }
  html, body {
    width: 1200px; height: 1000px; overflow: hidden;
    background: var(--backdrop);
    font-family: "Oswald", sans-serif;
  }
  .card {
    position: absolute;
    left: 205px; width: 790px;
  }
  .card--front { top: 30px; height: 455px; background: var(--card-black); }
  .card--back { top: 510px; height: 450px; background: var(--card-kraft); }

  .wordmark {
    position: absolute; left: 0; right: 0;
    text-align: center; font-weight: 400; text-transform: uppercase;
    line-height: 1;
  }
  .card--front .wordmark { top: 38px; color: var(--copper); }
  .card--back .wordmark { top: 100px; color: var(--ink-dark); }
  .wordmark__name { display: block; }
  .card--front .wordmark__name { font-size: 78px; letter-spacing: 1px; }
  .card--front .wordmark__sub { display: block; font-size: 30px; letter-spacing: 9px; margin-top: 6px; }
  .card--back .wordmark__name { font-size: 110px; letter-spacing: 2px; }
  .card--back .wordmark__sub { display: block; font-size: 42px; letter-spacing: 12px; margin-top: 6px; }

  .rule {
    position: absolute; left: 115px; width: 558px; height: 2px;
    background: var(--rule-grey);
  }
  .rule--top { top: 206px; }
  .rule--bottom { top: 392px; }

  .contact-list {
    position: absolute; left: 205px; top: 216px;
    list-style: none; color: var(--copper);
    font-size: 29px; font-weight: 400;
  }
  .contact-item { height: 42px; display: flex; align-items: center; position: relative; padding-left: 50px; }
  .contact-item__icon { position: absolute; left: 0; width: 30px; height: 26px; fill: var(--copper); }

  .services {
    position: absolute; left: 0; right: 0; top: 348px;
    text-align: center; color: var(--ink-dark);
    font-size: 24px; font-weight: 600; text-transform: uppercase;
    word-spacing: 1px;
  }
  .services__dot { margin: 0 9px; }
</style>
</head>
<body>

<section class="card card--front" aria-label="Card front">
  <div class="wordmark">
    <span class="wordmark__name">Ironvale</span>
    <span class="wordmark__sub">Barbers</span>
  </div>
  <div class="rule rule--top"></div>
  <ul class="contact-list">
    <li class="contact-item">42 KOWHAI ROAD, TAUPO</li>
    <li class="contact-item">
      <svg class="contact-item__icon" viewBox="0 0 30 26" aria-hidden="true"><path d="M8 3c1.5-1 3 0 3.4 1.2l1 3c.3 1-.2 1.7-1 2.2l-1 .6c.8 2.6 2.6 5 5 6.4l.8-.9c.7-.7 1.5-.9 2.3-.5l2.7 1.5c1 .6 1.2 2 .3 3-1.5 1.8-3.5 2.6-5.6 1.6C10 18.8 5.8 13 5.5 7.3 5.4 5.5 6.4 4 8 3z"/></svg>
      (07) 548 9163
    </li>
    <li class="contact-item">
      <svg class="contact-item__icon" viewBox="0 0 30 26" aria-hidden="true" fill="none" stroke="#b38c66" stroke-width="1.6"><circle cx="14" cy="13" r="11"/><ellipse cx="14" cy="13" rx="5" ry="11"/><path d="M3 13h22M5 7.5h18M5 18.5h18M14 2v22"/></svg>
      www.ironvalebarbers.com
    </li>
    <li class="contact-item">
      <svg class="contact-item__icon" viewBox="0 0 30 26" aria-hidden="true"><path d="M1 5h28v17H1z"/><path d="M1 5l14 10L29 5" fill="none" stroke="#1b1a19" stroke-width="1.6"/></svg>
      hello@ironvale.co.nz
    </li>
  </ul>
  <div class="rule rule--bottom"></div>
</section>

<section class="card card--back" aria-label="Card back">
  <div class="wordmark">
    <span class="wordmark__name">Ironvale</span>
    <span class="wordmark__sub">Barbers</span>
  </div>
  <p class="services">
    Mens Haircare<span class="services__dot">•</span>Wet Shaving<span class="services__dot">•</span>Facials<span class="services__dot">•</span>Skin Prescriptions
  </p>
</section>

</body>
</html>
```